Web Design for a Biotech Consulting Firm

We need a web site design for a new business based in Philadelphia called Corventa Dx. This is a consulting firm that will serve medical diagnostics industry, which is part of the life science/healthcare industry focusing on developing and marketing products that help in early detection, monitoring or management of diseases. Our consulting firm will help medical diagnostic companies to overcome key challenges in designing, evaluating and marketing new products.Our company name is Corventa Dx. Corventa is Latin word for "something" Dx represents diagnostics. The idea behind the name is that we help companies to transform the original, early product ideas ("nothing") into "something"; which is a product with full clinical utility that will help to improve health and well-being.The web site should use the visual feel of the logo (attached), be modern, simple and clean looking and represent creativity, innovation, scientific thinking and progress.
Updates

Wix Design is acceptable

Industry/Entity Type

Biotechnology

Coding

Coded - Design and coding required

Number of Pages Required

1 page

Font styles to use
Sans Serif

Requirements
Must have
• simple, clean look couple of pages
Should not have
• a lot of pages

```html
<!DOCTYPE html>
<html lang="en">
<head>
<meta charset="utf-8">
<title>Corventa Dx — Biotech Consulting</title>
<link href="https://fonts.googleapis.com/css2?family=Montserrat:wght@400;500;600;700&family=Lato:wght@400;700&display=swap" rel="stylesheet">
<style>
:root{
  --blue:#1a6cf5;
  --blue-deep:#1458d6;
  --ink:#1c1c1c;
  --text:#333;
  --muted:#555;
  --gray-bg:#f2f2f2;
  --dark:#1b1b1b;
  --white:#fff;
}
*{box-sizing:border-box;margin:0;padding:0}
html,body{width:1200px;height:3911px;overflow:hidden;background:var(--white)}
body{position:relative;font-family:'Lato',sans-serif;color:var(--text)}
.abs{position:absolute}
h1,h2,h3,.mont{font-family:'Montserrat',sans-serif;font-weight:400;color:var(--ink)}
.body-copy{font-size:11.5px;line-height:21px;color:var(--text)}

/* header */
.logo-box{left:172px;top:20px;width:72px;height:70px;border:2px solid var(--blue);display:flex;align-items:center;padding-left:8px;font-family:'Montserrat',sans-serif;font-size:15px;color:var(--ink);white-space:nowrap}
.call{right:173px;top:25px;font-family:'Montserrat',sans-serif;font-weight:700;font-size:19px;color:var(--blue);display:flex;align-items:center;gap:6px}
.nav{right:173px;top:72px;display:flex;gap:33px;font-family:'Montserrat',sans-serif;font-size:12.5px;color:#333;letter-spacing:.3px}
.nav .active{border-bottom:2px solid var(--blue);padding-bottom:4px}

/* hero */
.hero-left{left:0;top:114px;width:543px;height:541px;background:linear-gradient(135deg,#2a7bff,#1560ec)}
.hero-photo{left:543px;top:114px;width:657px;height:541px;background:linear-gradient(120deg,#c9b8a6,#8c7868 45%,#d8d4cf)}
.hero-title{left:172px;top:264px;font-family:'Montserrat',sans-serif;font-weight:700;font-size:56px;color:var(--white)}
.hero-sub{left:172px;top:343px;font-family:'Montserrat',sans-serif;font-size:22px;line-height:30px;color:var(--white)}
.btn{display:inline-flex;align-items:center;justify-content:center;font-family:'Montserrat',sans-serif;font-size:12px;font-weight:500;letter-spacing:.3px}
.btn-light{left:172px;top:424px;width:111px;height:32px;border:2px solid var(--white);color:var(--white)}
.dots{left:833px;top:617px;display:flex;gap:4px}
.dots span{width:9px;height:9px;background:var(--white)}

/* framed images */
.photo{border:5px solid var(--white);box-shadow:0 0 8px rgba(0,0,0,.25)}
.frame{border:6px solid var(--blue);border-right:none}
.frame::before,.frame::after{content:"";position:absolute;right:0;width:6px;background:var(--blue)}
.frame::before{top:-6px;height:100px}
.frame::after{bottom:-6px;height:100px}

.h-section{font-size:33px}
.sec-gray{left:0;top:1735px;width:1200px;height:612px;background:var(--gray-bg)}

/* cards */
.card{top:1966px;width:265px;height:264px;border:5px solid var(--blue);border-right:none;padding:40px 30px 0 30px}
.card::before,.card::after{content:"";position:absolute;right:0;width:5px;background:var(--blue)}
.card::before{top:-5px;height:82px}
.card::after{bottom:-5px;height:82px}
.card h3{font-size:15px;font-weight:500;margin:20px 0 12px}
.card p{font-size:11px;line-height:21px;color:var(--text)}

/* event */
.event-dark{left:0;top:3061px;width:675px;height:486px;background:var(--dark)}
.event-photo{left:675px;top:3061px;width:525px;height:486px;background:linear-gradient(135deg,#3a86ff,#1a5fe0 60%,#2f7bff)}
.date-box{left:172px;top:3161px;width:95px;height:91px;border:2px solid var(--blue);color:var(--blue);font-family:'Montserrat',sans-serif;font-size:19px;line-height:30px;text-align:center;padding-top:14px}

/* footer */
.foot-logo{left:172px;top:3620px;width:151px;height:149px;border:3px solid var(--blue);font-family:'Montserrat',sans-serif;font-size:31px;color:var(--ink);display:flex;align-items:center;padding-left:20px;white-space:nowrap}
.foot-h{font-family:'Montserrat',sans-serif;font-size:15px;color:#333}
.foot-list{font-size:11.5px;line-height:21px;color:#555;list-style:none}
.contact-item{display:flex;gap:14px;font-size:11px;line-height:17px;color:#555}
.rule{left:172px;top:3837px;width:855px;height:1px;background:#ddd}
.social{left:908px;top:3860px;display:flex;gap:6px}
.social span{width:25px;height:25px;border-radius:50%;background:var(--blue)}
</style>
</head>
<body>

<header>
  <div class="abs logo-box">Corventa Dx</div>
  <div class="abs call">
    <svg width="16" height="16" viewBox="0 0 24 24"><path fill="#1a6cf5" d="M6.6 10.8a15.1 15.1 0 0 0 6.6 6.6l2.2-2.2c.3-.3.7-.4 1-.2 1.1.4 2.3.6 3.6.6.6 0 1 .4 1 1V20c0 .6-.4 1-1 1A17 17 0 0 1 3 4c0-.6.4-1 1-1h3.5c.6 0 1 .4 1 1 0 1.3.2 2.5.6 3.6.1.3 0 .7-.2 1z"/></svg>
    CALL US:215.480.3172
  </div>
  <nav class="abs nav">
    <span class="active">HOME</span><span>ABOUT</span><span>SERVICES</span><span>PRODUCTS</span><span>NEWS</span><span>CONTACT</span>
  </nav>
</header>

<section>
  <div class="abs hero-left"></div>
  <div class="abs hero-photo" role="img" aria-label="Photo of three scientists discussing results at a lab table"></div>
  <h1 class="abs hero-title">Corventa Dx</h1>
  <p class="abs hero-sub">At vero eos et accusamus usto<br>odio dignissimos ducimias</p>
  <a class="abs btn btn-light">READ MORE</a>
  <div class="abs dots"><span></span><span></span><span></span><span></span><span></span></div>
</section>

<section>
  <div class="abs photo" style="left:217px;top:750px;width:327px;height:379px;background:linear-gradient(135deg,#dfe9ef,#a9c6d6 50%,#eef3f6)" role="img" aria-label="Photo of a lab researcher in mask holding a sample dish"></div>
  <div class="abs frame" style="left:172px;top:851px;width:310px;height:309px"></div>
  <h2 class="abs h-section" style="left:597px;top:806px">Welcome to Corventa Dx</h2>
  <p class="abs body-copy" style="left:600px;top:863px;width:420px">Lorem ipsum dolor sit amet, consectetur adipiscing elit, sed do eiusmod teor incididuLorem ipsum dolor sit amet, consectetur adipiscing elit, sed do eiusod tempor incididunt ut labore et dolore magna aliqua. Ut enim ad minim veniam, quis nostrud exercitation ullamco laboris nisi ut aliquip ex ea commodo consat. Duis aute irure dolor in reprehenderit in voluLorem ipsum dolor sit amet, cos ectetur adipiscing elit, sed do eiusmod tempor incididunt ut labore et dolore magna aliqu veniam, quis nostrud exercitation ullamco laboris nisi ut aliquip ex ea commodo consequat.</p>
</section>

<section>
  <h2 class="abs h-section" style="left:172px;top:1279px">Biotech Consulting</h2>
  <p class="abs body-copy" style="left:175px;top:1336px;width:420px">Lorem ipsum dolor sit amet, consectetur adipiscing elit, sed do eiusmod teor incididuLorem ipsum dolor sit amet, consectetur adipiscing elit, sed do eiusod tempor incididunt ut labore et dolore magna aliqua. Ut enim ad minim veniam, quis nostrud exercitation ullamco laboris nisi ut aliquip ex ea commodo consat. Duis aute irure dolor in reprehenderit in voluLorem ipsum dolor sit amet, cos ectetur adipiscing elit, sed do eiusmod tempor incididunt ut labore et dolore magna aliqu veniam, quis nostrud exercitation ullamco laboris nisi ut aliquip ex ea commodo consequat.</p>
  <div class="abs photo" style="left:694px;top:1224px;width:330px;height:376px;background:linear-gradient(135deg,#2b3e70,#c9d3df 45%,#f1f3f6)" role="img" aria-label="Photo of a scientist looking through a microscope"></div>
  <div class="abs frame" style="left:650px;top:1325px;width:310px;height:308px"></div>
</section>

<section>
  <div class="abs sec-gray"></div>
  <h2 class="abs h-section" style="left:0;width:1200px;text-align:center;top:1808px">What We Do</h2>
  <p class="abs body-copy" style="left:320px;width:560px;text-align:center;top:1863px">Lorem ipsum dolor sit amet, consectetur adipiscing elit, sed do eiusmod teor incididuLorem ipsum dolor sit amet, consetetur adipiscing elit, sed do eiusod tempor incididunt ut labore et dolore magna aliqua.</p>

  <div class="abs card" style="left:172px">
    <svg width="62" height="62" viewBox="0 0 62 62" fill="none" stroke="#1a6cf5" stroke-width="2"><circle cx="24" cy="24" r="18"/><circle cx="24" cy="24" r="11"/><circle cx="24" cy="24" r="3"/><path d="M37 37l18 18" stroke-width="4" stroke-linecap="round"/></svg>
    <h3>ATVERO EOS ETACCUS</h3>
    <p>Lorem ipsum dolor sit amet, consect etur adipiscing elit, sed do eiusmod te or incididuLorem ipsum dolo.</p>
  </div>
  <div class="abs card" style="left:468px">
    <svg width="62" height="62" viewBox="0 0 62 62" fill="none" stroke="#1a6cf5" stroke-width="2.5" stroke-linejoin="round"><path d="M31 52L9 30a12 12 0 0 1 22-16 12 12 0 0 1 22 16z"/><path d="M4 31h16l4-8 6 16 5-12 3 4h20"/></svg>
    <h3>ATVERO EOS ETACCUS</h3>
    <p>Lorem ipsum dolor sit amet, consect etur adipiscing elit, sed do eiusmod te or incididuLorem ipsum dolo.</p>
  </div>
  <div class="abs card" style="left:763px">
    <svg width="62" height="62" viewBox="0 0 62 62" fill="none" stroke="#1a6cf5" stroke-width="2.5" stroke-linecap="round"><path d="M12 56C20 40 40 22 50 6"/><path d="M6 48C20 46 30 26 44 8"/><path d="M14 44l8 6M20 36l10 6M26 28l10 6M32 20l10 6"/></svg>
    <h3>ATVERO EOS ETACCUS</h3>
    <p>Lorem ipsum dolor sit amet, consect etur adipiscing elit, sed do eiusmod te or incididuLorem ipsum dolo.</p>
  </div>
</section>

<section>
  <h2 class="abs h-section" style="left:0;width:1200px;text-align:center;top:2446px">Corventa Dx Product</h2>
  <div class="abs photo" style="left:217px;top:2541px;width:327px;height:376px;background:linear-gradient(135deg,#e87a5c,#efd6cc 40%,#b7c3d6)" role="img" aria-label="Photo of a technician preparing a patient for a scan"></div>
  <div class="abs frame" style="left:172px;top:2640px;width:310px;height:310px"></div>
  <h3 class="abs" style="left:597px;top:2563px;font-size:22px;line-height:30px">At vero eos et accusamus etusto<br>odio dignissimos ducimias</h3>
  <p class="abs body-copy" style="left:600px;top:2643px;width:420px">Lorem ipsum dolor sit amet, consectetur adipiscing elit, sed do eiusmod teor incididuLorem ipsum dolor sit amet, consectetur adipiscing elit, sed do eiusod tempor incididunt ut labore et dolore magna aliqua. Ut enim ad minim veniam, quis nostrud exercitation ullamco laboris nisi ut aliquip ex ea commodo consat. Duis aute irure dolor in reprehenderit in voluLorem ipsum dolor sit amet, cos ectetur adipiscing elit, sed do eiusmod tempor incididunt ut labore et dolore magna aliqu veniam, quis nostrud exercitation ullamco laboris nisi ut aliquip ex ea commodo consequat.</p>
  <a class="abs btn" style="left:600px;top:2828px;width:111px;height:37px;border:2px solid var(--blue);color:var(--blue)">READ MORE</a>
</section>

<section>
  <div class="abs event-dark"></div>
  <div class="abs event-photo" role="img" aria-label="Blue-toned photo of a clinician reviewing scan images on monitors"></div>
  <div class="abs date-box">June<br>08, 2019</div>
  <h3 class="abs" style="left:289px;top:3152px;font-size:22px;line-height:30px;color:var(--white)">At vero eos et accusamusto<br>odio dignissimos ducias</h3>
  <p class="abs body-copy" style="left:293px;top:3230px;width:350px;color:#e6e6e6">Lorem ipsum dolor sit amet, consectetur adipiscing elit, sed smod teor incididuLorem ipsum dolor sit amet, consectetur adipiscined do eiusod tempor incididunt ut labore et dolore magna alienim d minim veniam, quis nostrud exercitation ullamco laboris nisiquipex ea commodo consat. Duis aute irure dolor in reprehenderiuorem ipsum dolor sit amet, cos ectetur adipiscing elit, sed do d tempor incididunt ut labore et dolore magna aliqu veniam, qu loreexer citation ullamco laboris nisi ut aliqu.</p>
  <a class="abs btn" style="left:293px;top:3418px;width:111px;height:36px;border:2px solid var(--blue);color:var(--blue)">READ MORE</a>
</section>

<footer>
  <div class="abs foot-logo">Corventa Dx</div>

  <h4 class="abs foot-h" style="left:412px;top:3612px">CONTACT</h4>
  <div class="abs" style="left:412px;top:3648px;display:flex;flex-direction:column;gap:18px">
    <div class="contact-item"><svg width="22" height="22" viewBox="0 0 24 24" fill="none" stroke="#1a6cf5" stroke-width="1.5"><path d="M12 22s7-7 7-12a7 7 0 0 0-14 0c0 5 7 12 7 12z"/><circle cx="12" cy="10" r="2.5"/></svg><span>412 Larkwell Street,<br>Eastmoor, Philadelphia</span></div>
    <div class="contact-item"><svg width="22" height="22" viewBox="0 0 24 24" fill="none" stroke="#1a6cf5" stroke-width="1.5"><path d="M6.6 10.8a15.1 15.1 0 0 0 6.6 6.6l2.2-2.2c.3-.3.7-.4 1-.2 1.1.4 2.3.6 3.6.6.6 0 1 .4 1 1V20c0 .6-.4 1-1 1A17 17 0 0 1 3 4c0-.6.4-1 1-1h3.5c.6 0 1 .4 1 1 0 1.3.2 2.5.6 3.6.1.3 0 .7-.2 1z"/></svg><span>215 480 3172<br>215 480 3190</span></div>
    <div class="contact-item"><svg width="22" height="22" viewBox="0 0 24 24" fill="none" stroke="#1a6cf5" stroke-width="1.5"><rect x="3" y="6" width="18" height="13"/><path d="M3 6l9 7 9-7"/></svg><span>hello@corventadx.test<br>team@corventadx.test</span></div>
  </div>

  <h4 class="abs foot-h" style="left:665px;top:3612px">SERVICES</h4>
  <ul class="abs foot-list" style="left:665px;top:3643px">
    <li>Lorem ipsum dolo</li><li>Consectetur adipiscing elit.</li><li>Fusce eget leo tincid</li><li>Donec consequat</li><li>Praesent elementum</li><li>Jmauris posueret</li><li>Aenean a ex euctu</li>
  </ul>

  <h4 class="abs foot-h" style="left:884px;top:3612px">OTHER LINKS</h4>
  <ul class="abs foot-list" style="left:884px;top:3643px">
    <li>Lorem ipsum dolo</li><li>Consectetur adipiscing elit.</li><li>Fusce eget leo tincid</li><li>Donec consequat</li><li>Praesent elementum</li><li>Jmauris posueret</li><li>Aenean a ex euctu</li>
  </ul>

  <div class="abs rule"></div>
  <p class="abs" style="left:175px;top:3864px;font-size:12px;color:#444">Copyright 2019 All Rights Reserved</p>
  <div class="abs social" aria-label="Social links"><span></span><span></span><span></span><span></span></div>
</footer>

</body>
</html>
```